Recruitment Agency Needs a Core Values Wall for Office

Hello! We are hoping to reach out to the designer community to help us with achieving a wall in our office that beautifully presents our core values, so thanks for stopping by!
We are in a corporate office, but our median age in the office is 28 years old. For this reason we want the design to be fun, young and colourful while showing some sophistication.
The wall will be visible to the staff (within the open plan office), and the right colours will need to be used to enhance mood and productivity. Perhaps we could be looking at a colour for each core value? Or potentially some other way for each value to stand out?
The background doesn't have to be a specific colour. We would like some options to see how it will reflect in the office.
In terms of size - we aren't 100% on what size we are wanting to do it... but work within 1500x2700mm and we can work off that.
Fonts can be experimented with, without being too overpowering to the eye.
It needs to be clear, punchy and stand out from across the office (while being easy on the eye).
I have attached two images that can be used as inspiration. We would like more colour throughout the design.
The core values that will be required to be displayed:
Stop. Think. Challenge the Norm.
Our Detail is Our Difference.
Best Intentions. ALWAYS.
Turn Up, Turn On! Make ..it Happen!
Support Like Family. Party Like Rockstars.
Median staff age of 28, corporate office
Recruitment

```html
<!DOCTYPE html>
<html lang="en">
<head>
<meta charset="utf-8">
<title>Core Values Wall</title>
<link rel="stylesheet" href="https://fonts.googleapis.com/css2?family=Oswald:wght@300&family=Lobster&family=Josefin+Sans:wght@400&family=Roboto+Slab:wght@700&family=Montserrat:ital,wght@0,600;1,900&family=Playfair+Display:wght@400;500&family=Raleway:wght@300&family=Alfa+Slab+One&display=swap">
<style>
  :root {
    --page: #f4f4f4;
    --navy: #243a52;
    --yellow: #f5d33f;
    --coral: #e05a3c;
    --peach: #fbc7a8;
    --orange: #f07a33;
    --orange-dark: #c9571f;
    --white: #ffffff;
  }
  * { margin: 0; padding: 0; box-sizing: border-box; }
  html, body { width: 1200px; height: 1000px; overflow: hidden; background: var(--page); }
  .values-wall {
    position: absolute; left: 340px; top: 30px;
    width: 520px; height: 940px;
    background: var(--navy);
    overflow: hidden;
  }
  .wall-shapes { position: absolute; inset: 0; }
  .value {
    position: absolute; left: -200px; right: -200px;
    text-align: center; line-height: 1; white-space: nowrap;
  }
  .value-stop {
    top: 1px; font: 300 116px "Oswald", sans-serif; color: var(--yellow);
    transform: scaleX(0.86); letter-spacing: 1px;
  }
  .value-challenge { top: 170px; font: 400 56px "Lobster", cursive; color: var(--coral); }
  .value-detail { top: 248px; font: 400 42px "Josefin Sans", sans-serif; color: var(--yellow); letter-spacing: 1px; }
  .value-difference {
    top: 267px; font: 700 112px "Roboto Slab", serif; color: var(--peach);
    transform: scaleX(0.57); letter-spacing: -1px;
  }
  .value-intentions { top: 414px; font: 600 30px "Montserrat", sans-serif; color: var(--white); letter-spacing: 3px; }
  .value-always { top: 460px; font: italic 900 74px "Montserrat", sans-serif; color: var(--yellow); }
  .value-turn { font: 500 44px "Playfair Display", serif; color: var(--yellow); letter-spacing: 1px; }
  .value-turn-up { top: 550px; }
  .value-turn-on { top: 602px; }
  .value-make { top: 670px; font: 400 48px "Lobster", cursive; color: var(--orange); }
  .value-support { top: 738px; font: 300 40px "Raleway", sans-serif; color: var(--peach); }
  .value-party { top: 801px; font: 600 33px "Montserrat", sans-serif; color: var(--yellow); letter-spacing: 5px; }
  .value-rockstars { top: 838px; font: 400 60px "Alfa Slab One", serif; color: var(--orange); letter-spacing: 1px; }
</style>
</head>
<body>
  <main class="values-wall">
    <svg class="wall-shapes" width="520" height="940" viewBox="0 0 520 940" aria-hidden="true">
      <g class="dotted-rule" stroke="var(--coral)" stroke-width="2" stroke-dasharray="2 4">
        <line x1="45" y1="155" x2="475" y2="155"/>
        <line x1="45" y1="541" x2="475" y2="541"/>
      </g>
      <g class="ribbon">
        <polygon points="45,398 66,428 45,458 95,458 95,398" fill="var(--orange-dark)"/>
        <polygon points="475,398 454,428 475,458 425,458 425,398" fill="var(--orange-dark)"/>
        <polygon points="58,402 462,402 450,428 462,454 58,454 70,428" fill="var(--orange)"/>
      </g>
      <g class="turn-bands" fill="var(--peach)">
        <polygon points="45,565 152,565 146,592 45,592"/>
        <polygon points="368,565 475,565 475,592 374,592"/>
        <polygon points="45,617 152,617 146,644 45,644"/>
        <polygon points="368,617 475,617 475,644 374,644"/>
      </g>
      <g class="diamonds" fill="var(--peach)">
        <rect x="69" y="694" width="11" height="11" transform="rotate(45 74.5 699.5)"/>
        <rect x="440" y="694" width="11" height="11" transform="rotate(45 445.5 699.5)"/>
      </g>
      <g class="party-rules" stroke="var(--yellow)" stroke-width="1.5">
        <line x1="45" y1="817" x2="122" y2="817"/>
        <line x1="122" y1="809" x2="122" y2="825"/>
        <line x1="398" y1="817" x2="475" y2="817"/>
        <line x1="398" y1="809" x2="398" y2="825"/>
      </g>
    </svg>

    <p class="value value-stop">STOP. THINK</p>
    <p class="value value-challenge">Challenge the Norm</p>
    <p class="value value-detail">OUR DETAIL IS OUR</p>
    <p class="value value-difference">DIFFERENCE.</p>
    <p class="value value-intentions">BEST INTENTIONS</p>
    <p class="value value-always">ALWAYS.</p>
    <p class="value value-turn value-turn-up">TURN UP</p>
    <p class="value value-turn value-turn-on">TURN ON!</p>
    <p class="value value-make">Make…it Happen</p>
    <p class="value value-support">SUPPORT LIKE FAMILY.</p>
    <p class="value value-party">PARTY LIKE</p>
    <p class="value value-rockstars">ROCKSTARS.</p>
  </main>
</body>
</html>
```